Legal firm website redesign

Existing site for Sydney CBD lawyer needs clean and professional redesign - http://brennicklaw.com.au

The site will be viewed by a wide range of users: businesses, individuals, referral partners and other lawyers.

Please see the list of must haves for further details

Target Market(s)

Businesses, individuals, referral partners and other lawyers

Industry/Entity Type

Lawyer

Requirements
Must have
• Prominent display of phone number.
List of services down the left hand side of the site (5x services or so).
Search box in header.
Please use the greys and blues from the existing header.
New header must include the wording "Efficiency - Fulfillment - Integrity - Teamwork"

```html
<!DOCTYPE html>
<html lang="en">
<head>
<meta charset="utf-8">
<title>Brennick Law</title>
<link rel="stylesheet" href="https://fonts.googleapis.com/css2?family=Roboto+Condensed:wght@400;700&family=PT+Serif&family=Open+Sans:wght@400&display=swap">
<style>
:root{
  --page-bg:#5c5c5c;
  --panel-bg:#7b7b7b;
  --panel-line:#a3a3a3;
  --nav-grey:#9b9b9b;
  --nav-grey-dark:#8d8d8d;
  --blue-light:#6cc3e0;
  --blue:#3f9fc3;
  --band-blue:rgba(86,170,200,.82);
  --white:#ffffff;
  --heading:#303030;
  --body-text:#d9d9d9;
  --hero-top:#4a2a22;
  --hero-mid:#7a5a42;
  --hero-bottom:#d8b070;
}
*{margin:0;padding:0;box-sizing:border-box}
html,body{width:1200px;height:806px;overflow:hidden}
body{position:relative;background:var(--page-bg);font-family:"Open Sans",sans-serif;color:var(--white)}
.logo{position:absolute;left:168px;top:22px;font-family:"Roboto Condensed",sans-serif;font-weight:700;font-size:46px;color:var(--white);letter-spacing:.5px}
.phone{position:absolute;left:555px;top:46px;display:flex;align-items:center;gap:10px;font-family:"PT Serif",serif;font-size:16px;color:var(--white)}
.search{position:absolute;left:752px;top:30px;width:296px;height:54px;border:1px solid var(--panel-line);background:#666}
.search-input{position:absolute;left:11px;top:12px;width:192px;height:28px;background:var(--white);border:1px solid #ccc}
.search-button{position:absolute;left:211px;top:12px;width:74px;height:28px;background:linear-gradient(var(--blue-light),var(--blue));font-family:"Roboto Condensed",sans-serif;font-size:17px;color:var(--white);text-align:center;line-height:28px}
.main{position:absolute;left:137px;top:97px;width:911px;height:635px;background:var(--panel-bg);border:1px solid var(--panel-line)}
.nav{position:absolute;left:10px;top:10px;list-style:none}
.nav li{width:179px;height:37px;margin-bottom:11px;border-radius:3px;background:linear-gradient(var(--nav-grey),var(--nav-grey-dark));font-family:"Roboto Condensed",sans-serif;font-size:20px;line-height:37px;padding-left:22px;color:var(--white)}
.nav li.active{background:linear-gradient(var(--blue-light),var(--blue))}
.hero{position:absolute;left:202px;top:11px;width:699px;height:229px;border-radius:4px;overflow:hidden;background:linear-gradient(180deg,var(--hero-top) 0%,var(--hero-mid) 45%,var(--hero-bottom) 100%)}
.tagline{position:absolute;left:141px;top:31px;right:0;height:42px;background:var(--band-blue);border-radius:6px 0 0 6px;font-family:"Roboto Condensed",sans-serif;font-size:30px;line-height:42px;padding-left:24px;color:var(--white);word-spacing:4px}
.dots{position:absolute;left:617px;top:211px;display:flex;gap:8px}
.dots span{width:12px;height:12px;border-radius:50%;background:#9fd2e3}
.dots span:first-child{background:var(--blue)}
.section-title{font-family:"Roboto Condensed",sans-serif;font-size:20px;color:var(--heading);margin-bottom:14px}
.about{position:absolute;left:30px;top:266px;width:470px}
.about p{font-size:11px;line-height:24.3px;color:var(--body-text)}
.divider{position:absolute;left:527px;top:266px;width:1px;height:328px;background:#8c8c8c}
.recent{position:absolute;left:563px;top:266px;width:330px}
.recent ul{list-style:none}
.recent li{font-size:11px;line-height:24.3px;color:var(--body-text)}
.footer-nav{position:absolute;left:164px;top:748px;font-size:11.5px;color:var(--white)}
.footer-nav span{margin:0 7px}
.copyright{position:absolute;right:177px;top:748px;font-size:11.5px;color:var(--white)}
</style>
</head>
<body>
<div class="logo">brennick law</div>
<div class="phone">
  <svg width="22" height="16" viewBox="0 0 22 16" aria-hidden="true"><path d="M2 5 Q11 -1 20 5 L18 8 L15 6 L15 4 Q11 2 7 4 L7 6 L4 8 Z" fill="#bbb"/><rect x="5" y="8" width="12" height="7" rx="2" fill="#bbb"/></svg>
  (02) 9046 3172
</div>
<div class="search"><div class="search-input"></div><div class="search-button">Search</div></div>

<div class="main">
  <ul class="nav">
    <li class="active">Home</li>
    <li>About us</li>
    <li>Areas of Law</li>
    <li>Publications</li>
    <li>Contact</li>
  </ul>
  <div class="hero" role="img" aria-label="Open law books and reading glasses on a desk in front of a legal library">
    <div class="tagline">Efficiency. Fulfillment. Integrity. Teamwork.</div>
    <div class="dots"><span></span><span></span><span></span><span></span></div>
  </div>

  <div class="about">
    <h2 class="section-title">About Brennick Law</h2>
    <p>&nbsp;&nbsp;Brennick Law is a dynamic commercial law firm in the CBD of Sydney providing services to corporate, small business and private clients.</p>
    <p>&nbsp;&nbsp;Brennick Law brings together over 30 years of experience in legal practice.</p>
    <p>The strong focus of the firm is on commercial law and estate planning.</p>
    <p>&nbsp;&nbsp;Brennick Law is committed to providing quality legal services in helping its clients achieve their objectives by providing a proactive understanding of its clients' businesses and creative legal solutions.</p>
  </div>
  <div class="divider"></div>
  <div class="recent">
    <h2 class="section-title">Recent Additions</h2>
    <ul>
      <li>Commencement of the Succession Act 2006 25.03.08</li>
      <li>Is that will valid? 15.01.08</li>
      <li>Labor's proposed changes to IR laws 14.12.07</li>
      <li>Should you make your own will? 14.11.07</li>
      <li>Illegal workers 14.08.07</li>
      <li>Employees' liability for misleading or deceptive conduct 14.08.07</li>
      <li>Correct use of ACNs and ABNs 14.08.07</li>
      <li>Power of Attorney Infosheet 10.08.07</li>
      <li>Intestate Estates Infosheet 08.08.07</li>
      <li>Estate Planning Infosheet 07.06.07</li>
      <li>Special Disability Trusts Infosheet 18.05.07</li>
      <li>Testamentary Trusts Infosheet 17.05.07</li>
      <li>Appointment of an Enduring Guardian Infosheet 15.05.07</li>
    </ul>
  </div>
</div>

<div class="footer-nav">Home<span>|</span>About Us<span>|</span>Area of Law<span>|</span>Our People<span>|</span>Publication<span>|</span>Contact</div>
<div class="copyright">© 2012 BrennickLaw.com All Rights Reserved.</div>
</body>
</html>
```